VORN Selfie Wall Design for Coworking Space

Design a striking, large-scale wall mural for VORN Space that embodies our brand identity, incorporates Oakland-inspired elements, and enhances our coworking and event space. The design should be bold, visually engaging, and aligned with our brand aesthetic—featuring black, white, and bronze tones.
Key Requirements:
Branded Mural Design
Prominently (but tastefully) feature the VORN Space logo.
Use abstract shapes, gradients, or geometric patterns (inspired by the VORN logo) to convey movement and connectivity.
Incorporate the tagline: “Live · Work · Play · Go” in brand-approved typography.
Avoid literal imagery—keep the design sleek and modern.
Integrated Selfie Wall
Designate a photo-friendly zone with:
Open negative space (clean background) for people to pose naturally.
A bold but simple focal point (e.g., stylized typography, an Oakland-inspired icon, or a bronze metallic accent).
Lighting-friendly elements (avoid small patterns that may clash on camera).
Oakland Nods
Subtle references to the city (e.g., abstract skyline, bridge motifs, or topographic patterns) without being literal.
Updates
After reviewing designs, management has asked that this design incorporates a "selfie" aspect where people would be encouraged to take a photo with the wall. This would leave a thoughtful area for people to pose or engage with the design on the wall. Ideally, we want people to see the wall and take a picture with the design as a background
Target Market(s)
Office Employees
Industry/Entity Type
Real Estate/Coworking
Font styles to use
Other font styles liked:
- Henderson Sans
Look and feel
Each slider illustrates characteristics of the customer's brand and the style your logo design should communicate.

```html
<!DOCTYPE html>
<html lang="en">
<head>
<meta charset="utf-8">
<title>VORN Space — Selfie Wall Mural</title>
<link rel="stylesheet" href="https://fonts.googleapis.com/css2?family=Montserrat:wght@700&display=swap">
<style>
  :root {
    --canvas-bg: #e9e7e4;
    --mural-black: #0c0b0a;
    --bronze: #d49468;
    --bronze-deep: #6e4e33;
    --bronze-mid: #9c7550;
    --gold-light: #d6c59c;
    --smoke: #2a2520;
    --glow: #f4ead8;
    --brand-white: #ffffff;
  }
  html, body {
    margin: 0;
    width: 1068px;
    height: 1200px;
    overflow: hidden;
    background: var(--canvas-bg);
  }
  .mural {
    position: absolute;
    left: 0;
    top: 398px;
    width: 1068px;
    height: 404px;
    display: block;
  }
  .tagline-word {
    font-family: "Montserrat", sans-serif;
    font-weight: 700;
    font-size: 64px;
    letter-spacing: 6px;
    fill: var(--bronze);
  }
  .brand-name {
    font-family: "Montserrat", sans-serif;
    font-weight: 700;
    font-size: 110px;
    letter-spacing: 10px;
    fill: var(--brand-white);
  }
</style>
</head>
<body>
<svg class="mural" viewBox="0 0 1819 688" xmlns="http://www.w3.org/2000/svg">
  <defs>
    <linearGradient id="field-left" gradientUnits="userSpaceOnUse" x1="0" y1="688" x2="1000" y2="0">
      <stop offset="0" stop-color="var(--bronze-deep)"/>
      <stop offset="0.45" stop-color="var(--gold-light)"/>
      <stop offset="0.75" stop-color="var(--bronze-mid)"/>
      <stop offset="1" stop-color="var(--smoke)"/>
    </linearGradient>
    <linearGradient id="field-right" gradientUnits="userSpaceOnUse" x1="900" y1="688" x2="1900" y2="0">
      <stop offset="0" stop-color="var(--smoke)"/>
      <stop offset="0.35" stop-color="var(--bronze-mid)"/>
      <stop offset="0.6" stop-color="var(--gold-light)"/>
      <stop offset="1" stop-color="var(--bronze-deep)"/>
    </linearGradient>
    <filter id="glow" x="-20%" y="-20%" width="140%" height="140%">
      <feGaussianBlur stdDeviation="6" result="blur"/>
      <feMerge><feMergeNode in="blur"/><feMergeNode in="SourceGraphic"/></feMerge>
    </filter>
  </defs>

  <rect class="mural-ground" width="1819" height="688" fill="var(--mural-black)"/>

  <g class="stripe-fields" role="img" aria-label="Diagonal bronze and gold stripe pattern">
    <polygon class="stripe-field-left" points="380,0 1000,0 312,688 -308,688" fill="url(#field-left)"/>
    <polygon class="stripe-field-right" points="1560,0 2160,0 1472,688 872,688" fill="url(#field-right)"/>
    <polygon class="stripe-field-corner" points="2400,0 2600,0 1912,688 1712,688" fill="url(#field-right)"/>
  </g>

  <polygon class="selfie-zone" points="575,385 935,25 1245,335 885,695" fill="var(--mural-black)"/>

  <g class="glow-lines" stroke="var(--glow)" stroke-width="5" stroke-linecap="round" filter="url(#glow)">
    <line x1="945" y1="35" x2="1290" y2="380"/>
    <line x1="540" y1="335" x2="885" y2="680"/>
  </g>

  <text class="brand-name" x="915" y="400" text-anchor="middle">VORN</text>

  <g class="tagline">
    <text class="tagline-word" transform="translate(135 165) rotate(-45)" text-anchor="middle" dominant-baseline="middle">LIVE</text>
    <text class="tagline-word" transform="translate(1140 145) rotate(45)" text-anchor="middle" dominant-baseline="middle">PLAY</text>
    <text class="tagline-word" transform="translate(655 560) rotate(45)" text-anchor="middle" dominant-baseline="middle">WORK</text>
    <text class="tagline-word" transform="translate(1665 575) rotate(-45)" text-anchor="middle" dominant-baseline="middle">GO</text>
  </g>
</svg>
</body>
</html>
```